Mushroom Packaging - will require space for UPC code and other disclosures.

We are seeking to make packaging labels for our mushrooms.

Target Market(s)

Retail packaging label - there will be 20 different labels. We wish assistance on many different iterations changing the words and colors to differentiat new products

Industry/Entity Type

Retail mushroom packaging

Logo Text

Brand name is Meadow and Plate - space for label specifics as shown in examples

Logo styles of interest
Pictorial/Combination Logo
Requirements
Must have
• Must be a 2 inch by 3 inch label and must say product of USA, keep refridgerated, Make the name of the products most important part
Nice to have
• Ability to work with deisgner after the project is complete.
Should not have
• small fonts for the type of product. Please start with Sliced Shiitake Mushrooms Later we will add varations for other types such as Crimini Portabella Shiitake Oyster King Trumpets

```html
<!DOCTYPE html>
<html lang="en">
<head>
<meta charset="utf-8">
<title>Meadow and Plate – Sliced Shiitake Mushrooms Labels</title>
<link rel="stylesheet" href="https://fonts.googleapis.com/css2?family=Open+Sans:wght@600;700;800&family=Open+Sans+Condensed:wght@700&display=swap">
<style>
  :root {
    --page: #ffffff;
    --label-black: #111111;
    --label-gold: #f6b94b;
    --label-green: #12963e;
    --label-white: #ffffff;
    --tag-ink: #111111;
  }
  html, body {
    margin: 0;
    padding: 0;
    width: 1200px;
    height: 796px;
    overflow: hidden;
    background: var(--page);
  }
  .sheet {
    position: relative;
    width: 1200px;
    height: 796px;
  }
  .label {
    position: absolute;
    width: 436px;
    height: 290px;
  }
  .label--one { left: 115px; top: 71px; }
  .label--two { left: 653px; top: 71px; }
  .label--three { left: 384px; top: 450px; }

  .label .rim { fill: var(--label-black); }
  .label .edge { fill: var(--label-gold); }
  .label .field { fill: var(--label-green); }
  .label .brand {
    fill: var(--label-white);
    font-family: "Open Sans", sans-serif;
    font-weight: 800;
    font-size: 15px;
    letter-spacing: 0.5px;
  }
  .label .tag { fill: var(--label-gold); }
  .label .tag-text {
    fill: var(--tag-ink);
    font-family: "Open Sans Condensed", "Open Sans", sans-serif;
    font-weight: 700;
    font-size: 17px;
  }
  .label .product-name {
    fill: var(--label-white);
    font-family: "Open Sans", sans-serif;
    font-weight: 700;
    font-size: 46px;
  }
  .label .disclosure {
    fill: var(--label-white);
    font-family: "Open Sans Condensed", "Open Sans", sans-serif;
    font-weight: 700;
    font-size: 8.5px;
  }
  .label .net-weight {
    fill: var(--label-white);
    font-family: "Open Sans Condensed", "Open Sans", sans-serif;
    font-weight: 700;
    font-size: 12px;
  }
  .label .weight-box { fill: var(--label-white); }
  .label .web {
    fill: var(--label-white);
    font-family: "Open Sans", sans-serif;
    font-weight: 700;
    font-size: 8.5px;
  }
</style>
</head>
<body>
<main class="sheet">

  <svg class="label label--one" viewBox="0 0 400 266" aria-label="Sliced Shiitake Mushrooms label">
    <ellipse class="rim" cx="200" cy="133" rx="200" ry="133"/>
    <ellipse class="edge" cx="200" cy="131" rx="190" ry="122"/>
    <ellipse class="field" cx="200" cy="131" rx="186" ry="118"/>
    <text class="brand" x="200" y="38" text-anchor="middle">MEADOW AND PLATE</text>
    <g transform="rotate(-8 44 86)">
      <rect class="tag" x="16" y="73" width="58" height="26" rx="2"/>
      <text class="tag-text" x="45" y="92" text-anchor="middle">SLICED</text>
    </g>
    <text class="product-name" x="202" y="118" text-anchor="middle">Shiitake</text>
    <text class="product-name" x="202" y="165" text-anchor="middle">Mushrooms</text>
    <text class="disclosure" x="102" y="186">PRODUCT OF USA</text>
    <text class="disclosure" x="102" y="198">Keep Refridgerated</text>
    <text class="net-weight" x="119" y="216">NET WT.</text>
    <rect class="weight-box" x="196" y="178" width="104" height="42"/>
    <text class="web" x="200" y="238" text-anchor="middle">www.meadow-plate.com</text>
  </svg>

  <svg class="label label--two" viewBox="0 0 400 266" aria-label="Sliced Shiitake Mushrooms label">
    <ellipse class="rim" cx="200" cy="133" rx="200" ry="133"/>
    <ellipse class="edge" cx="200" cy="131" rx="190" ry="122"/>
    <ellipse class="field" cx="200" cy="131" rx="186" ry="118"/>
    <text class="brand" x="200" y="38" text-anchor="middle">MEADOW AND PLATE</text>
    <g transform="rotate(-8 44 86)">
      <rect class="tag" x="16" y="73" width="58" height="26" rx="2"/>
      <text class="tag-text" x="45" y="92" text-anchor="middle">SLICED</text>
    </g>
    <text class="product-name" x="202" y="118" text-anchor="middle">Shiitake</text>
    <text class="product-name" x="202" y="165" text-anchor="middle">Mushrooms</text>
    <text class="disclosure" x="102" y="186">PRODUCT OF USA</text>
    <text class="disclosure" x="102" y="198">Keep Refridgerated</text>
    <text class="net-weight" x="119" y="216">NET WT.</text>
    <rect class="weight-box" x="196" y="178" width="104" height="42"/>
    <text class="web" x="200" y="238" text-anchor="middle">www.meadow-plate.com</text>
  </svg>

  <svg class="label label--three" viewBox="0 0 400 266" aria-label="Sliced Shiitake Mushrooms label">
    <ellipse class="rim" cx="200" cy="133" rx="200" ry="133"/>
    <ellipse class="edge" cx="200" cy="131" rx="190" ry="122"/>
    <ellipse class="field" cx="200" cy="131" rx="186" ry="118"/>
    <text class="brand" x="200" y="38" text-anchor="middle">MEADOW AND PLATE</text>
    <g transform="rotate(-8 44 86)">
      <rect class="tag" x="16" y="73" width="58" height="26" rx="2"/>
      <text class="tag-text" x="45" y="92" text-anchor="middle">SLICED</text>
    </g>
    <text class="product-name" x="202" y="118" text-anchor="middle">Shiitake</text>
    <text class="product-name" x="202" y="165" text-anchor="middle">Mushrooms</text>
    <text class="disclosure" x="102" y="186">PRODUCT OF USA</text>
    <text class="disclosure" x="102" y="198">Keep Refridgerated</text>
    <text class="net-weight" x="119" y="216">NET WT.</text>
    <rect class="weight-box" x="196" y="178" width="104" height="42"/>
    <text class="web" x="200" y="238" text-anchor="middle">www.meadow-plate.com</text>
  </svg>

</main>
</body>
</html>
```